Re-design of Business Card

We require a design for our business card.

Quorin is a supplier of industrial packaging specializing in plastic products. We are undergoing a rebranding to appear more corporate. We have changed our company name to quorin and have a new logo.

I have uploaded our old card design with the previous company name.
Don't copy the current design. We are looking for a new design.

Industry/Entity Type

Manufacturing

Contact Information for Business Card

please don't copy the current design. we are looking for a new design.

Font styles to use
Sans Serif

Colors

Designer to choose colors to be used in the design.

Requirements
Must have
• clean and easy to read.

```html
<!DOCTYPE html>
<html lang="en">
<head>
<meta charset="utf-8">
<title>Quorin Business Card</title>
<link href="https://fonts.googleapis.com/css2?family=Roboto:wght@400;700;900&display=swap" rel="stylesheet">
<style>
  :root {
    --bg: #8a8a8a;
    --charcoal: #2b2b2b;
    --orange: #f47b20;
    --white: #ffffff;
  }
  * { margin: 0; padding: 0; box-sizing: border-box; }
  html, body { width: 1200px; height: 900px; overflow: hidden; }
  body {
    background: var(--bg);
    font-family: "Roboto", Arial, sans-serif;
    position: relative;
  }
  .card {
    position: absolute;
    left: 280px;
    width: 640px;
    height: 366px;
    overflow: hidden;
    box-shadow: 0 6px 18px rgba(0,0,0,0.35);
  }
  .card-front { top: 64px; background: var(--charcoal); }
  .card-back { top: 470px; background: var(--white); }

  .front-name {
    position: absolute;
    top: 118px; left: 0; right: 0;
    text-align: center;
    color: var(--orange);
    font-weight: 900;
    font-size: 72px;
    letter-spacing: 2px;
  }
  .front-rule {
    position: absolute;
    top: 290px; left: 40px; right: 40px;
    display: flex; align-items: center; gap: 14px;
  }
  .front-rule .line { flex: 1; height: 1px; background: var(--orange); }
  .front-rule .web { color: var(--white); font-size: 15px; }
  .front-rule .web em { font-style: normal; color: var(--orange); }

  .back-panel { position: absolute; inset: 0; }
  .back-info {
    position: absolute;
    left: 40px; top: 46px;
    color: var(--white);
    font-size: 14px;
    line-height: 1.45;
  }
  .person-name { color: var(--orange); font-weight: 700; font-size: 24px; line-height: 1.1; }
  .person-role { font-size: 15px; margin-bottom: 8px; }
  .office-title { color: var(--orange); font-weight: 700; font-size: 20px; margin-top: 10px; margin-bottom: 2px; }
  .row { display: flex; align-items: flex-start; gap: 8px; }
  .row + .row { margin-top: 2px; }
  .icon { width: 15px; height: 15px; flex: none; margin-top: 2px; }
  .gap { margin-top: 8px; }
  .back-brand {
    position: absolute;
    right: 40px; top: 150px;
    width: 280px;
    text-align: center;
    color: var(--orange);
    font-weight: 900;
    font-size: 54px;
    letter-spacing: 2px;
  }
</style>
</head>
<body>

<section class="card card-front">
  <div class="front-name">QUORIN</div>
  <div class="front-rule">
    <span class="line"></span>
    <span class="web">www.<em>quorin</em>.com.au</span>
    <span class="line"></span>
  </div>
</section>

<section class="card card-back">
  <svg class="back-panel" width="640" height="366" viewBox="0 0 640 366">
    <polygon points="0,0 300,0 238,366 0,366" fill="#2b2b2b"/>
    <line x1="300" y1="0" x2="238" y2="366" stroke="#f47b20" stroke-width="4"/>
  </svg>

  <div class="back-info">
    <div class="person-name">DANA MERCER</div>
    <div class="person-role">Machinery Sales Manager</div>
    <div class="row">
      <svg class="icon" viewBox="0 0 16 16"><rect width="16" height="16" fill="#f47b20"/><path d="M4 3l2 0 1 3-1.5 1a6 6 0 0 0 3.5 3.5L10 9l3 1v2a1 1 0 0 1-1 1A9 9 0 0 1 3 4a1 1 0 0 1 1-1z" fill="#2b2b2b"/></svg>
      <span>XXXX XXX XXX</span>
    </div>
    <div class="row">
      <svg class="icon" viewBox="0 0 16 16"><rect width="16" height="16" fill="#f47b20"/><rect x="3" y="4.5" width="10" height="7" fill="none" stroke="#2b2b2b" stroke-width="1.3"/><path d="M3 4.5l5 4 5-4" fill="none" stroke="#2b2b2b" stroke-width="1.3"/></svg>
      <span>dana@quorin.com.au</span>
    </div>

    <div class="office-title">HEAD OFFICE</div>
    <div class="row">
      <svg class="icon" viewBox="0 0 16 16"><rect width="16" height="16" fill="#f47b20"/><path d="M8 2.5a3.5 3.5 0 0 1 3.5 3.5c0 2.6-3.5 7-3.5 7S4.5 8.6 4.5 6A3.5 3.5 0 0 1 8 2.5z" fill="#2b2b2b"/><circle cx="8" cy="6" r="1.3" fill="#f47b20"/></svg>
      <span>12 Harbour Rd<br>Eastfield Park, Qld<br>4000 Australia</span>
    </div>
    <div class="row gap">
      <svg class="icon" viewBox="0 0 16 16"><rect width="16" height="16" fill="#f47b20"/><path d="M4 3l2 0 1 3-1.5 1a6 6 0 0 0 3.5 3.5L10 9l3 1v2a1 1 0 0 1-1 1A9 9 0 0 1 3 4a1 1 0 0 1 1-1z" fill="#2b2b2b"/></svg>
      <span>1300 000 418</span>
    </div>
    <div class="row">
      <svg class="icon" viewBox="0 0 16 16"><rect width="16" height="16" fill="#f47b20"/><rect x="4" y="3" width="8" height="4" fill="#2b2b2b"/><rect x="3" y="7.5" width="10" height="5.5" fill="#2b2b2b"/></svg>
      <span>+61 7 5550 0142</span>
    </div>
    <div class="row">
      <svg class="icon" viewBox="0 0 16 16"><rect width="16" height="16" fill="#f47b20"/><circle cx="8" cy="8" r="4.8" fill="none" stroke="#2b2b2b" stroke-width="1.2"/><path d="M3.2 8h9.6M8 3.2c-2.4 2.8-2.4 6.8 0 9.6M8 3.2c2.4 2.8 2.4 6.8 0 9.6" fill="none" stroke="#2b2b2b" stroke-width="1"/></svg>
      <span>www.quorin.com.au</span>
    </div>
  </div>

  <div class="back-brand">QUORIN</div>
</section>

</body>
</html>
```